New Business Cards for Velmora

About Velmora:
At Velmora, we're more than just a company—we're a force for positive change in the staffing industry. Our brand is our heartbeat, and we need a designer who can translate that into every design element.

The Project:
We're revamping our business cards and need your artistic flair to make them stand out. Here's what we're looking for:

- Incorporate our existing brand elements (logo, colours, fonts) into the design.
- Craft a design that's sleek, professional, and memorable.
- Provide options for different layouts and finishes.
- Collaborate closely with our team to ensure the final product exceeds expectations.

Please note: For general text, we use Avenir. The brand guidelines are slightly out of date and don't have correct imaging. Colours are correct though.

```html
<!DOCTYPE html>
<html lang="en">
<head>
<meta charset="utf-8">
<title>Velmora Business Cards</title>
<link href="https://fonts.googleapis.com/css2?family=Questrial&display=swap" rel="stylesheet">
<style>
  :root {
    --plum-deep: #3f0f4c;
    --plum: #5a1763;
    --plum-mid: #7a1d72;
    --magenta: #c8126f;
    --magenta-bright: #e0157a;
    --card-white: #ffffff;
    --paper-grey: #ececec;
    --ink: #3d0f4d;
    --backdrop: #e6e2de;
  }
  * { margin: 0; padding: 0; box-sizing: border-box; }
  html, body {
    width: 1200px; height: 900px; overflow: hidden;
    background: var(--backdrop);
    font-family: "Questrial", "Avenir", sans-serif;
  }
  .canvas {
    position: relative; width: 1200px; height: 900px;
    display: flex; flex-direction: column; align-items: center; justify-content: center; gap: 50px;
  }
  .card {
    position: relative; width: 560px; height: 320px; overflow: hidden;
    background: linear-gradient(135deg, var(--card-white) 40%, var(--paper-grey));
    box-shadow: 0 12px 30px rgba(40, 20, 30, 0.25);
  }

  /* Back card */
  .card-back { display: flex; flex-direction: column; align-items: center; }
  .card-back .wordmark { margin-top: 98px; font-size: 44px; line-height: 1; color: var(--ink); }
  .card-back .rule {
    margin-top: 22px; width: 420px; height: 1.5px;
    background: linear-gradient(90deg, transparent, var(--plum-mid) 30%, var(--magenta) 55%, var(--plum-mid) 75%, transparent);
  }
  .card-back .web { margin-top: 12px; font-size: 22px; letter-spacing: 1.5px; color: var(--ink); }

  /* Front card */
  .card-front .waves { position: absolute; inset: 0; }
  .brand {
    position: absolute; right: 40px; top: 62px; text-align: right; color: var(--ink);
  }
  .brand .wordmark { font-size: 46px; line-height: 1; }
  .brand .tagline { font-size: 13px; margin-top: 8px; letter-spacing: 0.3px; }

  .contact { position: absolute; left: 44px; top: 150px; color: #f4e8f3; }
  .contact .name { font-size: 20px; color: var(--magenta-bright); letter-spacing: 0.5px; }
  .contact .role { font-size: 15px; margin-top: 1px; }
  .contact .lines { list-style: none; margin-top: 16px; }
  .contact .lines li { display: flex; align-items: center; gap: 9px; font-size: 14.5px; height: 21px; letter-spacing: 0.4px; }
  .contact .lines li.gap { margin-top: 12px; }
  .contact .icon { width: 14px; height: 14px; flex: none; }
</style>
</head>
<body>
<main class="canvas">

  <section class="card card-back" aria-label="Card back">
    <div class="wordmark">Velmora</div>
    <div class="rule"></div>
    <div class="web">velmora.com.au</div>
  </section>

  <section class="card card-front" aria-label="Card front">
    <svg class="waves" viewBox="0 0 560 320" width="560" height="320" aria-hidden="true">
      <defs>
        <linearGradient id="plumBase" x1="0" y1="0" x2="1" y2="1">
          <stop offset="0" stop-color="#45114f"/>
          <stop offset="0.6" stop-color="#4c1358"/>
          <stop offset="1" stop-color="#3c0e49"/>
        </linearGradient>
        <linearGradient id="upperSwell" x1="0" y1="0" x2="1" y2="1">
          <stop offset="0" stop-color="#d0167a"/>
          <stop offset="0.5" stop-color="#8a1a6c"/>
          <stop offset="1" stop-color="#5a1763" stop-opacity="0.4"/>
        </linearGradient>
        <linearGradient id="lowerSwell" x1="0" y1="0" x2="1" y2="0.4">
          <stop offset="0" stop-color="#6c1a6a"/>
          <stop offset="0.6" stop-color="#c8126f"/>
          <stop offset="1" stop-color="#d8147a"/>
        </linearGradient>
      </defs>
      <path d="M0,0 L215,0 C275,0 285,95 318,140 C345,172 405,150 470,172 C520,190 545,228 560,252 L560,320 L0,320 Z" fill="url(#plumBase)"/>
      <path d="M150,0 L215,0 C275,0 285,95 318,140 C265,155 215,120 185,70 C170,42 160,18 150,0 Z" fill="url(#upperSwell)"/>
      <path d="M318,140 C345,172 405,150 470,172 C520,190 545,228 560,252 L560,320 L320,320 C300,260 250,225 215,205 C260,190 290,170 318,140 Z" fill="url(#lowerSwell)"/>
      <path d="M215,0 C275,0 285,95 318,140 C345,172 405,150 470,172 C520,190 545,228 560,252" fill="none" stroke="#cfcfcf" stroke-width="2"/>
    </svg>

    <div class="brand">
      <div class="wordmark">Velmora</div>
      <div class="tagline">staffing made human</div>
    </div>

    <div class="contact">
      <div class="name">AARON BLAKE</div>
      <div class="role">Director</div>
      <ul class="lines">
        <li>
          <svg class="icon" viewBox="0 0 14 14" aria-hidden="true"><rect x="3.5" y="1" width="7" height="12" rx="1.2" fill="none" stroke="#e0157a" stroke-width="1.2"/><line x1="6" y1="11" x2="8" y2="11" stroke="#e0157a" stroke-width="1"/></svg>
          0412 555 038
        </li>
        <li>
          <svg class="icon" viewBox="0 0 14 14" aria-hidden="true"><path d="M3,1.5 L5,1.5 L6,4.5 L4.6,5.6 C5.3,7.2 6.8,8.7 8.4,9.4 L9.5,8 L12.5,9 L12.5,11 C12.5,12 11.7,12.6 10.8,12.5 C6,12 2,8 1.5,3.2 C1.4,2.3 2,1.5 3,1.5 Z" fill="#e0157a"/></svg>
          02 5550 1742
        </li>
        <li class="gap">
          <svg class="icon" viewBox="0 0 14 14" aria-hidden="true"><rect x="1" y="3" width="12" height="8.5" fill="#e0157a"/><path d="M1,3 L7,8 L13,3" fill="none" stroke="#45114f" stroke-width="1"/></svg>
          aaron@velmora.com.au
        </li>
        <li>
          <svg class="icon" viewBox="0 0 14 14" aria-hidden="true"><g fill="none" stroke="#e0157a" stroke-width="1"><circle cx="7" cy="7" r="5.7"/><ellipse cx="7" cy="7" rx="2.5" ry="5.7"/><line x1="1.3" y1="7" x2="12.7" y2="7"/><line x1="2.2" y1="4" x2="11.8" y2="4"/><line x1="2.2" y1="10" x2="11.8" y2="10"/></g></svg>
          velmora.com.au
        </li>
      </ul>
    </div>
  </section>

</main>
</body>
</html>
```